Thank you for shopping with us business card

We would like a thank you card for our rebranded business. We used to be "Kestrel Knacks" but are now "Kestrel Trinkets. Old thank you card and new logo will be attached for reference. New thank you card does not have to be same design as old thank you card, but please use new logo.
Mopsa URL is now kestreltrinkets.mopsa.com
Pictaloo is @Kestrel_Trinkets
Email is kestreltrinkets@mopsamail.com
Thank you!

Contact Information for Business Card

Mopsa site, email, Pictaloo

```html
<!DOCTYPE html>
<html lang="en">
<head>
<meta charset="utf-8">
<title>Kestrel Trinkets – Business Card</title>
<link rel="stylesheet" href="https://fonts.googleapis.com/css2?family=Crimson+Pro:wght@400&family=Poppins:wght@600&display=swap">
<style>
  :root {
    --ink: #0b0b0b;
    --paper: #ffffff;
    --backdrop: #d9d9d9;
    --pattern-tone: #8a8a8a;
  }
  * { margin: 0; padding: 0; box-sizing: border-box; }
  html, body { width: 1200px; height: 1200px; overflow: hidden; }
  body { background: var(--backdrop); position: relative; }

  .card {
    position: absolute;
    left: 150px;
    width: 900px;
    height: 526px;
    background: var(--paper);
    overflow: hidden;
  }
  .card--front { top: 56px; }
  .card--back { top: 616px; }

  /* Front */
  .trim-pattern {
    position: absolute;
    left: 0; top: 209px;
    width: 383px; height: 36px;
    background: linear-gradient(var(--paper), var(--pattern-tone));
    opacity: 0.55;
  }
  .name-panel {
    position: absolute;
    left: 0; top: 245px;
    width: 383px; height: 281px;
    background: var(--ink);
    color: var(--paper);
    font-family: "Crimson Pro", serif;
  }
  .name-panel__name {
    position: absolute;
    left: 120px; top: 106px;
    font-size: 38px;
    line-height: 1;
    white-space: nowrap;
  }
  .name-panel__role {
    position: absolute;
    left: 120px; top: 150px;
    font-size: 21px;
    line-height: 1;
  }

  .brand-lockup {
    position: absolute;
    left: 419px; top: 106px;
    height: 124px;
    display: flex;
    align-items: center;
  }
  .brand-lockup__mark {
    width: 70px; height: 70px;
    background: var(--ink);
  }
  .brand-lockup__divider {
    width: 2px; height: 115px;
    background: var(--ink);
    margin: 0 31px 0 56px;
  }
  .brand-name {
    font-family: "Poppins", sans-serif;
    font-weight: 600;
    color: var(--ink);
    text-transform: uppercase;
    letter-spacing: 0.5px;
  }
  .brand-lockup .brand-name {
    font-size: 36px;
    line-height: 1.15;
  }

  .contact-list {
    position: absolute;
    left: 445px; top: 332px;
    list-style: none;
    font-family: "Crimson Pro", serif;
    font-size: 22px;
    color: var(--ink);
  }
  .contact-list__item {
    display: flex;
    align-items: center;
    height: 34.5px;
  }
  .contact-list__icon {
    width: 13px; height: 13px;
    margin-right: 9px;
    flex: none;
  }

  /* Back */
  .back-mark {
    position: absolute;
    left: 370px; top: 130px;
    width: 160px; height: 160px;
    background: var(--ink);
  }
  .back-name {
    position: absolute;
    left: 0; right: 0; top: 405px;
    text-align: center;
    font-size: 42px;
    line-height: 1.2;
  }
</style>
</head>
<body>
  <section class="card card--front" aria-label="Business card front">
    <div class="trim-pattern" role="img" aria-label="Decorative row of small outlined squares"></div>
    <div class="name-panel">
      <p class="name-panel__name">Mara Quell</p>
      <p class="name-panel__role">President/CEO</p>
    </div>

    <div class="brand-lockup">
      <div class="brand-lockup__mark"></div>
      <div class="brand-lockup__divider"></div>
      <p class="brand-name">Kestrel<br>Trinkets</p>
    </div>

    <ul class="contact-list">
      <li class="contact-list__item">
        <svg class="contact-list__icon" viewBox="0 0 13 13" aria-hidden="true"><rect x="1" y="1" width="11" height="11" fill="var(--ink)"/></svg>
        @Kestrel_Trinkets
      </li>
      <li class="contact-list__item">
        <svg class="contact-list__icon" viewBox="0 0 13 13" aria-hidden="true"><rect x="0.5" y="2.5" width="12" height="8" fill="var(--ink)"/><path d="M1 3 L6.5 7.5 L12 3" fill="none" stroke="var(--paper)" stroke-width="1.2"/></svg>
        kestreltrinkets@mopsamail.com
      </li>
      <li class="contact-list__item">
        <svg class="contact-list__icon" viewBox="0 0 13 13" aria-hidden="true"><circle cx="6.5" cy="6.5" r="6" fill="var(--ink)"/><ellipse cx="6.5" cy="6.5" rx="2.6" ry="6" fill="none" stroke="var(--paper)" stroke-width="0.9"/><line x1="0.5" y1="6.5" x2="12.5" y2="6.5" stroke="var(--paper)" stroke-width="0.9"/></svg>
        kestreltrinkets.mopsa.com
      </li>
    </ul>
  </section>

  <section class="card card--back" aria-label="Business card back">
    <div class="back-mark"></div>
    <p class="brand-name back-name">Kestrel Trinkets</p>
  </section>
</body>
</html>
```